Business Card - connecting 2 souls and beggining the journey of self discovery

Logo on the front
with tag line

On the back list of services and contact details

Seminars
workshops
Coaching
podcasts

Daniel Porthwick
Health & Wellbeing Life Coach
0491 372 815
daniel@wovenpathwellness.example
wovenpathwellness.example

Industry/Entity Type

Life Coaching

Contact Information for Business Card

I like the use of colour from the logo to be used. I'm not a fan of white.

Requirements
Must have
• My tagline: The journey home starts with you
Nice to have
• Use of colour that is in the mind body soul logo

```html
<!DOCTYPE html>
<html lang="en">
<head>
<meta charset="utf-8">
<title>Woven Path Wellness – Business Card</title>
<link href="https://fonts.googleapis.com/css2?family=Oswald:wght@500&family=Open+Sans:wght@400&family=Mulish:wght@500&display=swap" rel="stylesheet">
<style>
  :root {
    --stage: #5a4030;
    --card-light: #ffffff;
    --card-dark: #000000;
    --ink: #555555;
    --ink-soft: #6a6a6a;
    --wordmark: #777777;
    --wordmark-dark: #8a8a8a;
    --tagline: #9a9a9a;
    --brand: #f08a5c;
    --purple: #8a4fb0;
    --pink: #f06a74;
    --orange: #f6a23a;
    --green: #8cc850;
    --teal: #3bb59a;
  }
  * { box-sizing: border-box; margin: 0; padding: 0; }
  html, body {
    width: 1200px; height: 1000px; overflow: hidden;
    background: var(--stage);
  }
  .card {
    position: absolute;
    left: 266px; width: 666px; height: 397px;
    border-radius: 22px;
    overflow: hidden;
  }
  .card--front { top: 74px; background: var(--card-light); }
  .card--back { top: 533px; background: var(--card-dark); }

  .brand-dot {
    position: absolute; left: 50%; border-radius: 50%;
    background: var(--brand);
  }
  .card--front .brand-dot { top: 38px; width: 116px; height: 116px; margin-left: -58px; }
  .card--back .brand-dot { top: 89px; width: 136px; height: 136px; margin-left: -68px; }

  .wordmark {
    position: absolute; left: 0; right: 0; text-align: center;
    font-family: "Mulish", sans-serif; font-weight: 500;
    letter-spacing: -0.8px;
  }
  .card--front .wordmark { top: 172px; font-size: 29px; color: var(--wordmark); }
  .card--back .wordmark { top: 240px; font-size: 34px; color: var(--wordmark-dark); }

  .person {
    position: absolute; right: 352px; top: 242px; text-align: right;
  }
  .person__name {
    font-family: "Oswald", sans-serif; font-weight: 500;
    font-size: 24px; color: var(--ink); text-transform: uppercase; line-height: 32px;
  }
  .person__role {
    font-family: "Open Sans", sans-serif; font-size: 16px; color: var(--ink-soft);
    margin-top: 4px;
  }
  .divider {
    position: absolute; left: 332px; top: 241px; width: 2px; height: 60px;
    background: var(--ink);
  }
  .contact {
    position: absolute; left: 348px; top: 236px; list-style: none;
    font-family: "Open Sans", sans-serif; font-size: 16px; color: var(--ink);
  }
  .contact li { display: flex; align-items: center; height: 23.5px; white-space: nowrap; }
  .contact svg { width: 14px; height: 14px; margin-right: 8px; fill: var(--ink); flex: none; }

  .services {
    position: absolute; left: 0; right: 0; top: 323px; text-align: center;
    font-family: "Open Sans", sans-serif; font-size: 16.5px; color: var(--ink);
    letter-spacing: 1px; word-spacing: 4px;
  }
  .colour-band {
    position: absolute; left: 0; bottom: 0; width: 666px; height: 33px;
    background: linear-gradient(90deg, var(--purple), var(--pink) 35%, var(--orange) 60%, var(--green) 80%, var(--teal));
  }

  .tagline {
    position: absolute; left: 0; right: 0; top: 348px; text-align: center;
    font-family: "Open Sans", sans-serif; font-size: 17px; color: var(--tagline);
    letter-spacing: 1px;
  }
</style>
</head>
<body>
  <section class="card card--front">
    <span class="brand-dot" aria-hidden="true"></span>
    <p class="wordmark">Woven Path Wellness</p>

    <div class="person">
      <p class="person__name">Daniel Porthwick</p>
      <p class="person__role">Health &amp; Wellbeing Life Coach</p>
    </div>
    <span class="divider" aria-hidden="true"></span>
    <ul class="contact">
      <li><svg viewBox="0 0 16 16" aria-hidden="true"><path d="M1 5c0-2 2-3 7-3s7 1 7 3v1h-3V5H4v1H1zM4 7h8l2 3v4H2v-4zm4 2a2 2 0 100 4 2 2 0 000-4z"/></svg>0491 372 815</li>
      <li><svg viewBox="0 0 16 16" aria-hidden="true"><path d="M1 3h14v10H1zm1.5 1.5L8 9l5.5-4.5z"/></svg>daniel@wovenpathwellness.example</li>
      <li><svg viewBox="0 0 16 16" aria-hidden="true"><path d="M8 1a7 7 0 100 14A7 7 0 008 1zm0 1.5a5.5 5.5 0 015.4 4.5H10.5A9 9 0 008 2.5zm-1 0A9 9 0 005.5 7H2.6A5.5 5.5 0 017 2.5zM2.6 8.5h2.9A9 9 0 007 13.5a5.5 5.5 0 01-4.4-5zm4.4 0h2a8 8 0 01-1 4 8 8 0 01-1-4z"/></svg>www.wovenpathwellness.example</li>
    </ul>

    <p class="services">Seminars - Workshops - Coaching - Podcasts</p>

    <div class="colour-band" role="img" aria-label="Decorative colour band in the brand's purple, pink, orange, green and teal tones"></div>
  </section>

  <section class="card card--back">
    <span class="brand-dot" aria-hidden="true"></span>
    <p class="wordmark">Woven Path Wellness</p>
    <p class="tagline">The journey home starts with you</p>
  </section>
</body>
</html>
```